Letter head for peronal trainer

Letter head top and bottom. Elite looking design that looks modern and prestigious for high end clients. Black, silver, reds etc. Attached are my business cards (2 x pdfs) and my website is: www.dariomokhtar.net for style/ideas

Needs to look good when printing and be locked onto the page when people use my word docs on the computer, I don't want it to be 'clickable' if you know what I mean. Needs to work in A4 in portrait (and in landscape, for programme cards). I need it to be editable for when I adjust the text myself. Needs my contact details and social media details and title personal trainer (Central London/Greenwich/Blackheath) and Online Distance Coaching. . A little picture at the bottom too if it works (Like the vest one)

```html
<!DOCTYPE html>
<html lang="en">
<head>
<meta charset="utf-8">
<title>Dario Mokhtar – Letterhead</title>
<link rel="stylesheet" href="https://fonts.googleapis.com/css2?family=Open+Sans:wght@400;600;700&display=swap">
<style>
  :root {
    --ink: #111111;
    --paper: #ffffff;
    --silver: #9a9a9a;
    --silver-light: #c9c9c9;
    --red: #d2202a;
    --text: #222222;
    --photo-dark: #2b2b2b;
    --photo-light: #b5b5b5;
  }
  * { margin: 0; padding: 0; box-sizing: border-box; }
  html, body { width: 900px; height: 1200px; overflow: hidden; background: #e6e6e6; }
  .letterhead {
    position: relative;
    width: 900px;
    height: 1200px;
    background: var(--paper);
    overflow: hidden;
    font-family: "Open Sans", Arial, sans-serif;
    color: var(--text);
  }
  .side-band { position: absolute; left: 0; top: 0; width: 900px; height: 1200px; }
  .masthead {
    position: absolute;
    left: 0; right: 0; top: 30px;
    text-align: center;
  }
  .brand-name {
    font-size: 52px;
    font-weight: 700;
    letter-spacing: 2px;
    line-height: 1;
    color: var(--silver);
    text-transform: uppercase;
  }
  .role {
    margin-top: 8px;
    font-size: 18px;
    font-weight: 400;
    color: var(--text);
  }
  .service {
    display: inline-block;
    margin-top: 6px;
    padding: 2px 12px;
    background: var(--ink);
    color: var(--red);
    font-size: 21px;
    font-weight: 600;
    letter-spacing: 0.3px;
    line-height: 1.2;
  }
  .trainer-photo {
    position: absolute;
    left: 44px;
    top: 975px;
    width: 132px;
    height: 225px;
    border-radius: 40px 40px 0 0;
    background: linear-gradient(180deg, var(--photo-light) 0%, #7a7a7a 55%, var(--photo-dark) 100%);
  }
  .contact {
    position: absolute;
    left: 0; right: 0;
    display: flex;
    justify-content: center;
    align-items: center;
    gap: 18px;
    font-size: 13.5px;
    color: var(--text);
  }
  .contact-primary { top: 1144px; padding-left: 40px; }
  .contact-social { top: 1170px; padding-left: 40px; }
  .contact-item { display: flex; align-items: center; gap: 7px; }
  .contact-item svg { width: 13px; height: 13px; fill: var(--ink); }
  .social-dot { width: 9px; height: 9px; border-radius: 50%; background: var(--ink); }
</style>
</head>
<body>
<main class="letterhead">
  <svg class="side-band" viewBox="0 0 900 1200" aria-hidden="true">
    <path d="M0,0 L96,0 C52,260 40,600 68,900 C80,1040 98,1140 104,1200 L0,1200 Z" fill="#b0b0b0"/>
    <path d="M0,0 L88,0 C44,260 32,600 60,900 C72,1040 90,1140 96,1200 L0,1200 Z" fill="var(--ink)"/>
  </svg>

  <header class="masthead">
    <h1 class="brand-name">Dario Mokhtar</h1>
    <p class="role">Personal Trainer (Central London/Greenwich/Blackheath)</p>
    <p class="service">ONLINE DISTANCE COACHING</p>
  </header>

  <div class="trainer-photo" role="img" aria-label="Black and white photo of the personal trainer, shirtless, standing with hands on hips"></div>

  <footer>
    <div class="contact contact-primary">
      <span class="contact-item">
        <svg viewBox="0 0 16 16"><path d="M3 1h3l1.5 4-2 1.2a9 9 0 0 0 4.3 4.3L11 8.5l4 1.5v3a2 2 0 0 1-2 2A12 12 0 0 1 1 3a2 2 0 0 1 2-2z"/></svg>
        07700 900418
      </span>
      <span class="contact-item">
        <svg viewBox="0 0 16 16"><path d="M1 4h14v9H1z M2.2 5 8 9.5 13.8 5z" fill-rule="evenodd"/></svg>
        mokhtar.pt@fitmail.net
      </span>
    </div>
    <div class="contact contact-social">
      <span class="contact-item"><span class="social-dot"></span>@dario_fit</span>
      <span class="contact-item"><span class="social-dot"></span>DarioMokhtarFitness</span>
      <span class="contact-item">
        <svg viewBox="0 0 16 16"><circle cx="8" cy="8" r="6.5" fill="none" stroke="#111" stroke-width="1.4"/><path d="M1.5 8h13M8 1.5c-3 3.5-3 9.5 0 13M8 1.5c3 3.5 3 9.5 0 13" fill="none" stroke="#111" stroke-width="1.2"/></svg>
        www.dariomokhtar.net
      </span>
    </div>
  </footer>
</main>
</body>
</html>
```